Bluecrest Automotive Service Website Design

We are working with Bluecrest Automotive Service. They are a local mechanic/garage and in need of a new website design.

Some sites to use for inspiration:

https://www.torvalcar.example
https://www.quenbo.example
https://pavels-carcare.example
https://www.ashgrovetotalautocare.example/

Thank you for taking the time to consider designing a website for us. We are web developers based in Stockton, CA, USA. Most of our projects go through the same process. Understanding this process may help you win a project with us. We custom-code all of our websites in-house. We don’t have any requirements as to what tools you use for your design, but we prefer Figma files. For any design that we label as four-stars, we send it to the client for review. The client picks the final design they want us to use. Once we complete this process, we will continue to show additional clients all the four-star sites and purchase them later. Your designs will have multiple chances to sell. For better chances of success, we ask that you follow these guidelines.

IMAGES:
If you use any images or icons in the design, we ask that you have a link to the asset so we can purchase the image/icon. Most of the designs we submit do not have the customer’s images on them unless they have some great images. Be creative; show us the feeling you are trying to portray with your image choices. Use any royalty-free site you choose. We subscribe to Adobe and mainly use their images, but we can purchase images outside of Adobe.

PLEASE NOTE: we will not submit designs to clients with watermarks on the images.

FONTS:
We ask that you identify the fonts used in the design. This can be done in a message if you want. We typically use Google Fonts and Adobe Fonts.

CONTENT:
We're always open to different content and ideas. We often submit designs with stock images so the client can see our vision. We typically take pictures after the website launch to use their images with our vision. Lorem Ipsum is fine for paragraphs, but we ask that you write the headers in correct English. We want to be able to show the vision and identify the sections of the website.

INSPIRATION:
We typically add a couple of links in the brief of websites we like to help you get started in your design.

REVISIONS:
We do not often ask for revisions of the designs unless we see something in the design that may not appeal to the client. If there are slight changes that we want to make, we do that in the development process.

FEEDBACK:
We rarely give feedback on designs during the design process. We are working on many website projects and do not have the time to provide feedback. We usually respond if your request is well thought out and asks specific questions, but a note asking “feedback, please” usually goes unanswered.

```html
<!DOCTYPE html>
<html lang="en">
<head>
<meta charset="utf-8">
<title>Bluecrest Automotive Service</title>
<link href="https://fonts.googleapis.com/css2?family=Inter:ital,wght@0,400;0,500;0,600;0,700;0,800;0,900;1,400;1,500;1,700;1,800&family=Oswald:wght@600&display=swap" rel="stylesheet">
<style>
  :root {
    --red: #b00c0f;
    --red-bright: #d4161b;
    --black: #050505;
    --ink: #111111;
    --white: #ffffff;
    --card: #f3f3f3;
    --grey-text: #8a8a8a;
  }
  * { box-sizing: border-box; margin: 0; padding: 0; }
  html, body { width: 1200px; height: 3009px; overflow: hidden; }
  body { position: relative; background: var(--white); font-family: "Inter", Arial, sans-serif; color: var(--ink); }
  .abs { position: absolute; }

  /* Top utility bar */
  .utility-bar { left: 0; top: 0; width: 1200px; height: 39px; background: var(--white); }
  .account-link { left: 778px; top: 11px; font-size: 14px; font-weight: 500; letter-spacing: 1.6px; display: flex; align-items: center; gap: 10px; }
  .schedule-button { left: 979px; top: 0; width: 221px; height: 39px; background: var(--red-bright); color: var(--white); font-family: "Oswald", "Arial Narrow", sans-serif; font-weight: 600; font-size: 20px; display: flex; align-items: center; justify-content: center; letter-spacing: 0.3px; }

  /* Main navigation */
  .main-nav { left: 0; top: 39px; width: 1200px; height: 95px; background: var(--black); }
  .brand-name { left: 155px; top: 30px; color: var(--white); font-weight: 800; font-size: 26px; letter-spacing: 0.5px; }
  .nav-links { left: 511px; top: 35px; display: flex; list-style: none; }
  .nav-links li { color: var(--white); font-size: 15px; padding: 0 15px; border-left: 1px solid #bbbbbb; line-height: 26px; }
  .nav-links li:first-child { border-left: none; }

  /* Hero */
  .hero { left: 0; top: 134px; width: 1200px; height: 407px; background: linear-gradient(90deg, #1b1510 0%, #6e4a26 22%, #a7784a 38%, #3a2a1c 52%, #0b0b0b 64%, #070707 100%); }
  .hero-title { right: 65px; top: 87px; text-align: right; color: var(--white); font-weight: 900; font-size: 42px; line-height: 42px; letter-spacing: -0.5px; }
  .hero-title .accent { color: var(--red-bright); }
  .hero-copy { right: 65px; top: 216px; text-align: right; color: var(--white); font-size: 15px; line-height: 18.5px; white-space: nowrap; }

  /* Locator */
  .locator-title { left: 0; top: 600px; width: 1200px; text-align: center; font-size: 40px; font-weight: 700; }
  .locator-input { left: 398px; top: 679px; width: 279px; height: 56px; border: 2px solid var(--ink); background: var(--white); padding-left: 22px; display: flex; align-items: center; color: var(--grey-text); font-size: 17px; }
  .locator-button { left: 677px; top: 679px; width: 126px; height: 56px; background: var(--red); color: var(--white); font-size: 20px; font-weight: 500; display: flex; align-items: center; justify-content: center; }

  /* Promotions */
  .promo-offer { left: 0; top: 808px; width: 600px; height: 410px; background: var(--black); color: var(--white); text-align: center; }
  .offer-big { left: 0; top: 72px; width: 600px; font-size: 82px; font-weight: 800; letter-spacing: -1px; line-height: 82px; }
  .offer-sub { left: 0; top: 160px; width: 600px; font-size: 25px; line-height: 30px; }
  .offer-cta { left: 0; top: 190px; width: 600px; font-size: 34px; font-weight: 800; font-style: italic; line-height: 35px; }
  .offer-note { left: 0; top: 262px; width: 600px; font-size: 16px; }
  .offer-button { left: 180px; top: 296px; width: 244px; height: 43px; border: 2px solid var(--red-bright); font-size: 20px; font-weight: 800; display: flex; align-items: center; justify-content: center; }
  .promo-tires { left: 600px; top: 808px; width: 600px; height: 410px; background: radial-gradient(circle at 40% 55%, #d8c49a 0%, #c2ae86 30%, #aaa395 55%, #8d8b88 100%); text-align: center; }
  .tires-title { left: 0; top: 92px; width: 600px; font-size: 43px; font-style: italic; font-weight: 400; line-height: 42px; color: var(--ink); }
  .tires-rule { top: 203px; width: 84px; height: 2px; background: var(--ink); }
  .tires-link { left: 0; top: 191px; width: 600px; font-size: 20px; font-weight: 700; color: var(--red); }
  .tires-copy { left: 0; top: 237px; width: 600px; font-size: 25px; line-height: 27px; color: var(--ink); }

  /* Services */
  .services { left: 0; top: 1218px; width: 1200px; height: 1338px; background: linear-gradient(180deg, #0b0b0b 0%, #2a2a2a 20%, #4a4d52 45%, #6d6f72 70%, #a9a9a9 88%, #3b3b3b 100%); }
  .service-card { text-align: center; }
  .service-card h2 { font-weight: 800; font-size: 34px; letter-spacing: -0.3px; }
  .service-card p { font-size: 15px; line-height: 33.5px; white-space: nowrap; }
  .card-featured { left: 137px; top: 1315px; width: 926px; height: 573px; background: var(--card); }
  .card-featured svg { position: absolute; left: 435px; top: 124px; }
  .card-featured h2 { position: absolute; left: 0; top: 200px; width: 926px; }
  .card-featured p { position: absolute; left: 0; top: 253px; width: 926px; }
  .card-brake { left: 137px; top: 1888px; width: 463px; height: 573px; background: var(--red); color: var(--white); }
  .card-oil { left: 600px; top: 1888px; width: 463px; height: 573px; background: var(--black); color: var(--white); }
  .card-half svg { position: absolute; left: 194px; top: 42px; }
  .card-half h2 { position: absolute; left: 0; top: 120px; width: 463px; }
  .card-half p { position: absolute; left: 0; top: 173px; width: 463px; }

  /* Footer */
  .footer-brand { left: 146px; top: 2640px; color: #8a8a8a; font-weight: 800; font-size: 50px; line-height: 54px; letter-spacing: -0.5px; }
  .footer-brand small { display: block; font-size: 20px; line-height: 26px; letter-spacing: 0.5px; }
  .footer-address { left: 465px; top: 2650px; color: var(--red); font-size: 20px; line-height: 33px; font-style: normal; }
  .footer-nav { left: 0; top: 2858px; width: 1200px; list-style: none; }
  .footer-nav li { position: absolute; top: 0; font-size: 20px; font-weight: 500; white-space: nowrap; }
  .footer-nav .current { color: var(--red); padding: 0 7px 5px; border-bottom: 2px solid var(--red); }
  .footer-rule { left: 472px; top: 2920px; width: 250px; height: 2px; background: #555555; }
  .footer-slogan { left: 0; top: 2950px; width: 1200px; text-align: center; color: var(--red); font-size: 19px; font-style: italic; font-weight: 500; letter-spacing: 3px; }
</style>
</head>
<body>

<header>
  <div class="abs utility-bar">
    <div class="abs account-link">Sign In / Register
      <svg width="13" height="8" viewBox="0 0 13 8"><path d="M1 1l5.5 5.5L12 1" fill="none" stroke="#111" stroke-width="1.8"/></svg>
    </div>
    <div class="abs schedule-button">SCHEDULE SERVICE</div>
  </div>
  <nav class="abs main-nav">
    <div class="abs brand-name">Bluecrest</div>
    <ul class="abs nav-links">
      <li>CLIENT FEEDBACK</li>
      <li>PROMOTIONS</li>
      <li>CONNECT</li>
      <li>VISIT US</li>
    </ul>
  </nav>
</header>

<section class="abs hero" role="img" aria-label="Close-up photo of a bronze car's front headlight and bumper in low light">
  <h1 class="abs hero-title">YOUR CAR DESERVES<br><span class="accent">EXPERT CARE</span>.</h1>
  <p class="abs hero-copy">Lorem ipsum dolor sit amet, consectetur adipiscing elit, sed do<br>eiusmod tempor incididunt ut labore et dolore magna aliqua.<br>Ut enim ad minim veniam, quis nostrud exercitation ullamco<br>laboris nisi ut aliquip ex ea commodo consequat.<br>Duis aute irure dolor in reprehenderit in voluptate velit<br>esse cillum dolore eu fugiat nulla pariatur.</p>
</section>

<section class="locator">
  <h2 class="abs locator-title">Is Bluecrest near to you?</h2>
  <div class="abs locator-input">ZIP Code, City, State</div>
  <div class="abs locator-button">GO!</div>
</section>

<section class="abs promo-offer">
  <div class="abs offer-big">10% OFF</div>
  <div class="abs offer-sub">YOUR FIRST SERVICE</div>
  <div class="abs offer-cta">BOOK ONLINE TODAY<br>AND SAVE INSTANTLY</div>
  <div class="abs offer-note">Conditions apply.</div>
  <div class="abs offer-button">SCHEDULE NOW</div>
</section>

<section class="abs promo-tires" role="img" aria-label="Faded photo of a gold alloy wheel and tire">
  <div class="abs tires-title">FREE TIRE ROTATION<br>WITH OIL CHANGE</div>
  <div class="abs tires-rule" style="left:119px"></div>
  <div class="abs tires-link">LEARN MORE</div>
  <div class="abs tires-rule" style="left:397px"></div>
  <div class="abs tires-copy">Keep your ride smooth and safe,<br>complimentary with every<br>full synthetic oil change.</div>
</section>

<section class="abs services" role="img" aria-label="Photo of an empty garage workshop with tall windows and a shutter door"></section>

<article class="abs service-card card-featured">
  <svg width="56" height="62" viewBox="0 0 56 62">
    <ellipse cx="34" cy="31" rx="18" ry="28" fill="none" stroke="#111" stroke-width="8"/>
    <path d="M24 5 C8 8 4 54 24 57" fill="none" stroke="#111" stroke-width="8"/>
    <path d="M14 16 h8 M10 31 h8 M14 46 h8" stroke="#f3f3f3" stroke-width="3"/>
  </svg>
  <h2>TIRE ROTATION</h2>
  <p>Lorem ipsum dolor sit amet, consectetur adipiscing elit. Curabitur dignissim, orci at sagittis scelerisque,<br>justo enim hendrerit justo, ut luctus neque tortor ac turpis. Vivamus vel urna non justo fermentum blandit.<br>Aenean vehicula, massa sit amet pretium varius, nibh quam scelerisque augue, sed convallis magna<br>urna ac lorem. Praesent semper, purus nec fermentum vehicula, nulla lacus tincidunt mauris,<br>sit amet scelerisque magna nisl in velit. Integer sit amet malesuada sapien. Vestibulum dictum lorem<br>nec pulvinar scelerisque.</p>
</article>

<article class="abs service-card card-half card-brake">
  <svg width="76" height="62" viewBox="0 0 76 62">
    <circle cx="38" cy="31" r="21" fill="none" stroke="#fff" stroke-width="6"/>
    <path d="M12 14 A30 30 0 0 0 12 48" fill="none" stroke="#fff" stroke-width="5"/>
    <path d="M64 14 A30 30 0 0 1 64 48" fill="none" stroke="#fff" stroke-width="5"/>
  </svg>
  <h2>BRAKE CHANGE</h2>
  <p>Lorem ipsum dolor sit amet, consectetur adipiscing<br>elit. Curabitur dignissim, orci at sagittis scelerisque,<br>justo enim hendrerit justo, ut luctus neque tortor ac<br>turpis. Vivamus vel urna non justo fermentum blandit.<br>Aenean vehicula, massa sit amet pretium varius,<br>nibh quam scelerisque augue, sed convallis magna<br>urna ac lorem. Praesent semper, purus nec<br>fermentum vehicula, nulla lacus tincidunt mauris,<br>sit amet scelerisque magna nisl in velit. Integer sit<br>amet malesuada sapien. Vestibulum dictum lorem<br>nec pulvinar scelerisque.</p>
</article>

<article class="abs service-card card-half card-oil">
  <svg width="76" height="62" viewBox="0 0 76 62">
    <path d="M30 7 A25 25 0 0 0 22 52" fill="none" stroke="#fff" stroke-width="4.5" stroke-linecap="round"/>
    <path d="M46 55 A25 25 0 0 0 56 12" fill="none" stroke="#fff" stroke-width="4.5" stroke-linecap="round"/>
    <path d="M52 6 l5 7 -8 2" fill="none" stroke="#fff" stroke-width="4" stroke-linecap="round"/>
    <path d="M25 58 l-4 -7 8 -1" fill="none" stroke="#fff" stroke-width="4" stroke-linecap="round"/>
    <circle cx="38" cy="5" r="2.6" fill="#fff"/><circle cx="46" cy="6" r="2.6" fill="#fff"/>
    <circle cx="30" cy="57" r="2.6" fill="#fff"/><circle cx="38" cy="58" r="2.6" fill="#fff"/>
  </svg>
  <h2>OIL CHANGE</h2>
  <p>Lorem ipsum dolor sit amet, consectetur adipiscing<br>elit. Curabitur dignissim, orci at sagittis scelerisque,<br>justo enim hendrerit justo, ut luctus neque tortor ac<br>turpis. Vivamus vel urna non justo fermentum blandit.<br>Aenean vehicula, massa sit amet pretium varius,<br>nibh quam scelerisque augue, sed convallis magna<br>urna ac lorem. Praesent semper, purus nec<br>fermentum vehicula, nulla lacus tincidunt mauris,<br>sit amet scelerisque magna nisl in velit. Integer sit<br>amet malesuada sapien. Vestibulum dictum lorem<br>nec pulvinar scelerisque.</p>
</article>

<footer>
  <div class="abs footer-brand">Bluecrest<small>AUTOMOTIVE SERVICE</small></div>
  <address class="abs footer-address">518 HARBOR WORKS LANE, SUITE 2C, EASTFIELD DISTRICT<br>GEARFORD CITY, 57204, REPUBLIC OF AUTOVIA</address>
  <ul class="abs footer-nav">
    <li class="current" style="left:131px">HOME</li>
    <li style="left:291px">CLIENT FEEDBACK</li>
    <li style="left:564px">PROMOTIONS</li>
    <li style="left:792px">CONNECT</li>
    <li style="left:983px">VISIT US</li>
  </ul>
  <div class="abs footer-rule"></div>
  <p class="abs footer-slogan">“Because Every Customer Deserves Exceptional Service.”</p>
</footer>

</body>
</html>
```